Bref créative
TMB Business Cards and Stationary
Professional
Marcus Elsby
General Manager
2716 Bellhaven Lane
Fernridge, CA 91987
marcus@tobinmillbuilders.example

```html
<!DOCTYPE html>
<html lang="en">
<head>
<meta charset="utf-8">
<title>TMB Corp Business Cards</title>
<link rel="stylesheet" href="https://fonts.googleapis.com/css2?family=Arimo:wght@400;700&display=swap">
<style>
  :root {
    --stage: #d9d9d9;
    --green: #2eaa1c;
    --green-dark: #1d8412;
    --green-light: #44c22e;
    --paper: #ffffff;
    --ink: #2b2b2b;
    --ink-soft: #5a5a5a;
  }
  * { box-sizing: border-box; margin: 0; padding: 0; }
  html, body {
    width: 1200px; height: 901px; overflow: hidden;
    background: var(--stage);
    font-family: "Arimo", Arial, sans-serif;
  }
  .stage { position: relative; width: 1200px; height: 901px; }
  .card {
    position: absolute; top: 296px;
    width: 540px; height: 309px;
    box-shadow: 0 8px 24px rgba(0,0,0,.18);
    overflow: hidden;
  }
  /* back face */
  .card-back {
    left: 40px;
    background: linear-gradient(135deg, var(--green-light) 0%, var(--green) 55%, var(--green-dark) 100%);
    display: flex; align-items: center; justify-content: center; gap: 18px;
  }
  .card-back .mark-dot {
    width: 86px; height: 86px; border-radius: 50%; background: var(--paper);
  }
  .card-back .mark-name {
    color: var(--paper); font-weight: 700; font-size: 46px; letter-spacing: 2px;
  }
  /* front face */
  .card-front { left: 620px; background: var(--paper); }
  .accent-tab {
    position: absolute; left: 0; top: 84px; width: 16px; height: 22px; background: var(--green);
  }
  .holder { position: absolute; left: 30px; top: 82px; }
  .holder-name { color: var(--green); font-weight: 700; font-size: 23px; line-height: 1.1; }
  .holder-title { color: var(--ink-soft); font-size: 12px; margin-top: 3px; }
  .address {
    position: absolute; left: 30px; top: 142px;
    color: var(--ink-soft); font-size: 11.5px; line-height: 1.35; font-style: normal;
  }
  .contacts {
    position: absolute; left: 196px; top: 196px; list-style: none;
    color: var(--ink-soft); font-size: 11.5px; line-height: 1;
  }
  .contacts li { display: flex; align-items: center; gap: 8px; height: 15px; }
  .contacts svg { width: 10px; height: 10px; fill: var(--green); flex: none; }
  .brand {
    position: absolute; right: 34px; top: 72px;
    display: flex; align-items: center; gap: 10px;
  }
  .brand-dot { width: 44px; height: 44px; border-radius: 50%; background: var(--green); }
  .brand-name { color: var(--ink); font-weight: 700; font-size: 30px; letter-spacing: 1px; }
</style>
</head>
<body>
<main class="stage">
  <section class="card card-back" aria-label="Card back">
    <span class="mark-dot"></span>
    <span class="mark-name">TMB</span>
  </section>

  <section class="card card-front" aria-label="Card front">
    <span class="accent-tab"></span>
    <div class="holder">
      <p class="holder-name">Marcus Elsby</p>
      <p class="holder-title">General Manager</p>
    </div>
    <address class="address">2716 Bellhaven Lane<br>Fernridge, CA 91987</address>
    <ul class="contacts">
      <li><svg viewBox="0 0 10 10"><path d="M2 0h2l1 3-1.5 1a6 6 0 0 0 2.5 2.5L7 5l3 1v2a2 2 0 0 1-2 2A8 8 0 0 1 0 2a2 2 0 0 1 2-2z"/></svg>555-014-2231</li>
      <li><svg viewBox="0 0 10 10"><rect x="1" y="3" width="8" height="5"/><rect x="2.5" y="0.5" width="5" height="2.5"/></svg>555-014-2298</li>
      <li><svg viewBox="0 0 10 10"><rect x="2.5" y="0" width="5" height="10" rx="1"/></svg>555-014-2376</li>
      <li><svg viewBox="0 0 10 10"><path d="M0 2h10v6H0z M0 2l5 3.5L10 2" /></svg>marcus@tobinmillbuilders.example</li>
    </ul>
    <div class="brand">
      <span class="brand-dot"></span>
      <span class="brand-name">TMB CORP</span>
    </div>
  </section>
</main>
</body>
</html>
```